Corporate Vision/Mission Designs for the Office Walls

What we are looking for:

We are looking for design proposals to frame our mission, vision and values on our office walls

The designs need to be elegant, clean lines, simple, easy to follow and of course, should follow our brand guidelines.

Here's the copy:

For Boardoom:
Vision: Marlow Brightside ignites people with passion enabling joy and lifetime memories

Mission: We are transforming the way property is bought.

For Garage
Purpose: We connect people with their dreams, turn dreams into reality.

For Entrance
Core Values
Honour
Passion
Sharing
Surprise
Fun

Vision & Mission will go in the boardroom
Core Values : at the Entrance
Purpose: in the Garage meeting room

Attachments to this project include:

a) Photos of the walls where they will go, and the current designs on the walls

b) brand guidelines

Industry/Entity Type

Office

Font styles to use
Decorative

Requirements
Must have
• Follow the brandguidelines, and colors.
• Green / use minimally

```html
<!DOCTYPE html>
<html lang="en">
<head>
<meta charset="utf-8">
<title>Purpose</title>
<link rel="stylesheet" href="https://fonts.googleapis.com/css2?family=Alegreya+Sans:ital,wght@0,400;1,400&family=Open+Sans:ital,wght@1,400&display=swap">
<style>
  :root {
    --accent: #14b3ae;
    --ink: #53575c;
    --paper-center: #ffffff;
    --paper-edge: #ececec;
  }
  html, body {
    margin: 0;
    padding: 0;
    width: 1200px;
    height: 848px;
    overflow: hidden;
  }
  .wall-panel {
    width: 1200px;
    height: 848px;
    background: radial-gradient(ellipse 62% 62% at 50% 50%, var(--paper-center) 35%, var(--paper-edge) 100%);
  }
  .wall-panel svg {
    display: block;
  }
  .heading {
    font-family: "Open Sans", "Segoe UI", sans-serif;
    font-style: italic;
    font-size: 84px;
    fill: var(--accent);
  }
  .rule {
    stroke: var(--accent);
    stroke-width: 2;
  }
  .statement {
    font-family: "Alegreya Sans", "Gill Sans", sans-serif;
    fill: var(--ink);
  }
  .statement-line {
    font-size: 46px;
  }
  .statement-spaced {
    font-size: 46px;
  }
  .statement-hero {
    font-style: italic;
    font-size: 136px;
  }
  .statement-small {
    font-style: italic;
    font-size: 46px;
  }
  .statement-close {
    font-style: italic;
    font-size: 98px;
  }
</style>
</head>
<body>
<main class="wall-panel">
  <svg width="1200" height="848" viewBox="0 0 1200 848" xmlns="http://www.w3.org/2000/svg">
    <text class="heading" x="600" y="254" text-anchor="middle">PURPOSE</text>
    <line class="rule" x1="336" y1="284" x2="864" y2="284"/>
    <g class="statement">
      <text class="statement-line" x="349" y="362" textLength="501" lengthAdjust="spacing">We connect people with</text>
      <text class="statement-spaced" x="370" y="436" textLength="460" lengthAdjust="spacing">their dreams, turn</text>
      <text class="statement-hero" x="380" y="556" textLength="444" lengthAdjust="spacing">dreams</text>
      <text class="statement-small" x="349" y="648" textLength="72" lengthAdjust="spacingAndGlyphs">into</text>
      <text class="statement-close" x="462" y="648" textLength="384" lengthAdjust="spacing">reality.</text>
    </g>
  </svg>
</main>
</body>
</html>
```